Verostel business card

Business card for sustainable investment company called "Verostel". Verostel is an exchange platform selling carbon credits between buyers and sellers. Carbon Credits are an environmental commodity for reducing global carbon emissions.

the card should obviously have our logo and the theme should be sustainability/environment mixed with a trading platform.

Contact Information for Business Card

Logo, Name, Title, Phone, Email

Colors
0054AA
0677BA
7BADD7
CADEEF
E8F1F8
0094D4
00A9DD
6FCCEA
C7EBF8
E9F6FB
00AB8E
00BBA5
67D7C9
C6EFE9
E9F9F6
59FF00
82FF00
B8FF75
E3FFCB
F4FFEA

```html
<!DOCTYPE html>
<html lang="en">
<head>
<meta charset="utf-8">
<title>Verostel business cards</title>
<link href="https://fonts.googleapis.com/css2?family=Anton&family=Work+Sans:wght@500;600&display=swap" rel="stylesheet">
<style>
  :root {
    --backdrop: #9e9e9e;
    --card: #ffffff;
    --ink: #231f20;
    --rule-warm: #4a3528;
  }
  * { margin: 0; padding: 0; box-sizing: border-box; }
  html, body { width: 1200px; height: 1116px; overflow: hidden; }
  body {
    background: var(--backdrop);
    position: relative;
    font-family: "Work Sans", Arial, sans-serif;
    color: var(--ink);
  }
  .card {
    position: absolute;
    width: 518px;
    height: 311px;
    background: var(--card);
  }
  .col-left { left: 63px; }
  .col-right { left: 617px; }
  .row-1 { top: 54px; }
  .row-2 { top: 397px; }
  .row-3 { top: 739px; }

  .brand {
    position: absolute;
    top: 40px;
    right: 35px;
    display: flex;
    align-items: center;
    gap: 7px;
    font-weight: 600;
    font-size: 20px;
    letter-spacing: 0.02em;
    color: var(--ink);
  }
  .brand-square { width: 14px; height: 14px; background: var(--ink); }

  .identity {
    position: absolute;
    top: 133px;
    left: 0;
    right: 0;
    display: flex;
    justify-content: center;
    align-items: stretch;
  }
  .person {
    text-align: right;
    padding-top: 1px;
  }
  .person-name {
    font-family: "Anton", Impact, sans-serif;
    font-size: 28px;
    line-height: 36px;
    letter-spacing: 0.035em;
    white-space: nowrap;
  }
  .person-title {
    font-weight: 500;
    font-size: 14.5px;
    line-height: 18px;
    letter-spacing: 0.04em;
  }
  .divider {
    width: 2px;
    height: 58px;
    background: var(--ink);
    margin: 0 21px;
  }
  .divider-warm { background: var(--rule-warm); }
  .contact { padding-top: 0; }
  .contact-phone {
    font-weight: 600;
    font-size: 16.5px;
    line-height: 20px;
    letter-spacing: 0.04em;
  }
  .contact-line {
    font-weight: 600;
    font-size: 13px;
    line-height: 19px;
    letter-spacing: 0.06em;
  }
</style>
</head>
<body>

<section class="card col-left row-1">
  <div class="brand"><span class="brand-square"></span>Verostel</div>
  <div class="identity">
    <div class="person"><div class="person-name">RAMI TAVAKOL</div><div class="person-title">Founder</div></div>
    <div class="divider"></div>
    <div class="contact"><div class="contact-phone">+4807215583</div><div class="contact-line">rami@verostel.com</div><div class="contact-line">verostel.com</div></div>
  </div>
</section>

<section class="card col-right row-1">
  <div class="brand"><span class="brand-square"></span>Verostel</div>
  <div class="identity">
    <div class="person"><div class="person-name">ERAN MALKIEL</div><div class="person-title">Founder</div></div>
    <div class="divider"></div>
    <div class="contact"><div class="contact-phone">+972504817326</div><div class="contact-line">Eran@verostel.com</div><div class="contact-line">verostel.com</div></div>
  </div>
</section>

<section class="card col-left row-2">
  <div class="brand"><span class="brand-square"></span>Verostel</div>
  <div class="identity">
    <div class="person"><div class="person-name">NIKOS STAVRIDIS</div><div class="person-title">Founder</div></div>
    <div class="divider"></div>
    <div class="contact"><div class="contact-phone">+36305281764</div><div class="contact-line">nikos@verostel.com</div><div class="contact-line">verostel.com</div></div>
  </div>
</section>

<section class="card col-right row-2">
  <div class="brand"><span class="brand-square"></span>Verostel</div>
  <div class="identity">
    <div class="person"><div class="person-name">OMER DAHAN</div><div class="person-title">Founder</div></div>
    <div class="divider"></div>
    <div class="contact"><div class="contact-phone">+36304926118</div><div class="contact-line">omer@verostel.com</div><div class="contact-line">verostel.com</div></div>
  </div>
</section>

<section class="card col-left row-3">
  <div class="brand"><span class="brand-square"></span>Verostel</div>
  <div class="identity">
    <div class="person"><div class="person-name">MIREILLE CASTAN</div><div class="person-title">Vice President</div></div>
    <div class="divider divider-warm"></div>
    <div class="contact"><div class="contact-phone">+33671529403</div><div class="contact-line">mc@verostel.com</div><div class="contact-line">verostel.com</div></div>
  </div>
</section>

<section class="card col-right row-3">
  <div class="brand"><span class="brand-square"></span>Verostel</div>
  <div class="identity">
    <div class="person"><div class="person-name">ITAI BRENNER</div><div class="person-title">Founder</div></div>
    <div class="divider"></div>
    <div class="contact"><div class="contact-phone">+36307614259</div><div class="contact-line">itai@verostel.com</div><div class="contact-line">verostel.com</div></div>
  </div>
</section>

</body>
</html>
```